Help me create an amazing cover for my first ebook!!

I am looking to have a modern and professional looking cover for my first ebook. It will be published through Borvex Quill Self Press and will need to follow their formatting and guidelines. I want the cover to have a modern and vibrant feel, that appeals to a millennial audience. This is a real estate book that is focused on a niche category catered to young professionals, so the idea would be to appeal to them.

Title:
The Twentysomething Playbook for Duplex Living

A Smart Property Buying Plan to Start Early, Cut Your Housing Costs (Sometimes to Zero), and Speed Up Your Path to Lasting Wealth.

Davin Osterlund

Target Market(s)

Real Estate investors, investors, millennials, young professionals, college educated, 20-40 years old.Financial freedom, finance.

Industry/Entity Type

Real Estate

Font styles to use
Sans Serif

Colors

Designer to choose colors to be used in the design.

Requirements
Must have
• Must follow the borvex quill self press format. I attached a screenshot of the details, it can also be found here: https://qsp.borvexbooks.example/en_US/help/topic/R481736025
• Must include this title:
• The Twentysomething Playbook for Duplex Living
• A Smart Property Buying Plan to Start Early, Cut Your Housing Costs (Sometimes to Zero), and Speed Up Your Path to Lasting Wealth.
• Davin Osterlund.
• I added examples of book covers I like to use as a guide, I also added some color pallette examples.
Nice to have
• Modern, clean design that's not too busy. Some sort of simple photo or illustration to incorporate in the cover along with the text would be nice.

```html
<!DOCTYPE html>
<html lang="en">
<head>
<meta charset="utf-8">
<title>The Twentysomething Playbook for Duplex Living</title>
<link href="https://fonts.googleapis.com/css2?family=Bebas+Neue&family=Cinzel:wght@700;900&display=swap" rel="stylesheet">
<style>
  :root {
    --title-red: #c0141e;
    --author-navy: #1e2a86;
    --subtitle-ink: #141210;
    --bg-light: #f6ead8;
    --bg-mid: #ead2b0;
    --bg-warm: #dcb98e;
    --bg-deep: #c49a6c;
    --photo-roof-light: #f0c48c;
    --photo-roof: #d9925a;
    --photo-roof-dark: #b86e3c;
    --photo-stack: #9c7a58;
    --photo-floor: #d8b48a;
  }
  * { margin: 0; padding: 0; box-sizing: border-box; }
  html, body {
    width: 776px;
    height: 1200px;
    overflow: hidden;
    background: var(--bg-light);
  }
  .cover {
    position: relative;
    width: 776px;
    height: 1200px;
    overflow: hidden;
    background: linear-gradient(180deg, var(--bg-light) 0%, var(--bg-mid) 45%, var(--bg-warm) 70%, var(--bg-mid) 85%, var(--bg-deep) 100%);
  }
  .cover-photo {
    position: absolute;
    top: 440px;
    left: 96px;
    width: 590px;
    height: 455px;
    border-radius: 6px;
    background:
      linear-gradient(180deg,
        var(--photo-roof-light) 0%,
        var(--photo-roof) 32%,
        var(--photo-roof-dark) 52%,
        var(--photo-stack) 70%,
        var(--photo-floor) 100%);
  }
  .book-title {
    position: absolute;
    top: 58px;
    left: 0;
    right: 0;
    text-align: center;
    font-family: "Bebas Neue", "Oswald", sans-serif;
    font-weight: 400;
    color: var(--title-red);
    letter-spacing: -1px;
    line-height: 104px;
  }
  .book-title .line { display: block; font-size: 108px; }
  .book-title .line-long { font-size: 88px; }
  .book-subtitle {
    position: absolute;
    top: 918px;
    left: 78px;
    right: 78px;
    text-align: center;
    font-family: "Cinzel", "Times New Roman", serif;
    font-weight: 900;
    font-size: 26px;
    line-height: 40px;
    color: var(--subtitle-ink);
  }
  .book-author {
    position: absolute;
    right: 8px;
    bottom: 0;
    font-family: "Bebas Neue", "Oswald", sans-serif;
    font-size: 92px;
    line-height: 1;
    letter-spacing: -1px;
    color: var(--author-navy);
  }
</style>
</head>
<body>
  <main class="cover">
    <h1 class="book-title">
      <span class="line line-long">The Twentysomething</span>
      <span class="line">Playbook for</span>
      <span class="line">Duplex Living</span>
    </h1>
    <div class="cover-photo" role="img" aria-label="Photograph of a banknote folded into a roof shape resting on two tall stacks of coins, with a short coin stack between them"></div>
    <p class="book-subtitle">A Smart Property Buying Plan to Start Early, Cut Your Housing Costs (Sometimes to Zero), and Speed Up Your Path to Lasting Wealth.</p>
    <p class="book-author">Davin Osterlund.</p>
  </main>
</body>
</html>
```